E-Sport banner for team [logo already created]

Hey,

Need a 2400 x 600 banner for our esport team we are creating.
The logo is already created, what we need is to make a banner out of it.

So, the logo shouldn't stay exactly the same, you should be creative and do something special with it.

Banner should be:
Clean
Modern
Have kinda the same theme as the logo provided
Be creative

Example of banners (not the same size):
https://img.pixovault.net/v/7kQ2mRtLpWa/fullsize.jpg
https://img.pixovault.net/v/Hn_beRoWz3c/fullsize.jpg
https://img.pixovault.net/v/qtmoYKdBvRs/fullsize.jpg
https://img.pixovault.net/v/gLP8wNnHxJd/fullsize.jpg

Check here for even more inspiration:
https://artlumora.com/tags/esports_banner

```html
<!DOCTYPE html>
<html lang="en">
<head>
<meta charset="utf-8">
<title>Kestra Gaming – E-Sportcenter Banner</title>
<link rel="stylesheet" href="https://fonts.googleapis.com/css2?family=Exo+2:wght@400&family=Saira:wght@500&display=swap">
<style>
  :root {
    --blue-core: #1d56bd;
    --blue-mid: #0f3a8f;
    --blue-deep: #061436;
    --streak: #6fc3ff;
    --mark-fill: #27324a;
    --mark-text: #dfe3ea;
    --wordmark: #c8ccd3;
    --accent: #f6e600;
  }
  * { margin: 0; padding: 0; box-sizing: border-box; }
  html, body { width: 1200px; height: 300px; overflow: hidden; background: var(--blue-deep); }
  .banner {
    position: relative;
    width: 1200px;
    height: 300px;
    overflow: hidden;
    background:
      radial-gradient(ellipse 70% 90% at 52% 50%, var(--blue-core) 0%, var(--blue-mid) 55%, var(--blue-deep) 100%);
  }
  .light-streak {
    position: absolute;
    left: 0;
    top: 126px;
    width: 420px;
    height: 4px;
    background: linear-gradient(90deg, rgba(111,195,255,0) 0%, rgba(111,195,255,0.55) 55%, rgba(200,235,255,0.9) 75%, rgba(111,195,255,0) 100%);
    filter: blur(1.5px);
  }
  .light-glow {
    position: absolute;
    left: 230px;
    top: 98px;
    width: 140px;
    height: 60px;
    background: radial-gradient(ellipse at center, rgba(120,200,255,0.45) 0%, rgba(120,200,255,0) 70%);
  }
  .team-mark {
    position: absolute;
    left: 150px;
    top: 58px;
    width: 180px;
    display: flex;
    flex-direction: column;
    align-items: center;
    gap: 14px;
  }
  .team-mark__badge {
    width: 120px;
    height: 120px;
    border-radius: 50%;
    background: var(--mark-fill);
  }
  .team-mark__name {
    font-family: "Exo 2", sans-serif;
    font-weight: 400;
    font-size: 26px;
    letter-spacing: 0.12em;
    color: var(--mark-text);
  }
  .wordmark {
    position: absolute;
    left: 412px;
    top: 76px;
    width: 625px;
    text-align: center;
    font-family: "Exo 2", sans-serif;
    font-weight: 400;
    font-size: 78px;
    line-height: 1;
    letter-spacing: 0.02em;
    color: var(--wordmark);
    white-space: nowrap;
  }
  .tagline {
    position: absolute;
    left: 412px;
    top: 193px;
    width: 625px;
    text-align: center;
    font-family: "Saira", sans-serif;
    font-weight: 500;
    font-size: 25px;
    letter-spacing: 0.38em;
    color: var(--accent);
    text-shadow: 0 0 6px rgba(246,230,0,0.45);
  }
</style>
</head>
<body>
  <main class="banner">
    <div class="light-streak"></div>
    <div class="light-glow"></div>

    <div class="team-mark">
      <div class="team-mark__badge"></div>
      <span class="team-mark__name">KESTRA</span>
    </div>

    <h1 class="wordmark">KESTRA GAMING</h1>
    <p class="tagline">E-SPORTCENTER</p>
  </main>
</body>
</html>
```